Orbell Consulting- executive coaching business

looking for business card design for a newly started coaching business.
specialising in Exective coaching, Leadership, NLP and Motivation.
Looking for a simple, classy design using the existing logo attached and colour themes that complement the logo.
No red or orange in the business card design please.

Target Market(s)

Defence and Veteran community

Industry/Entity Type

Life Coaching

Contact Information for Business Card

looking for business cards for newly started coaching business.
specialising in Exective Coaching, Leadership, NLP and Motivation

Font styles to use
Serif
Script

Colors
0556a4
3176b5
86cfc6
33b8a4

Requirements
Must have
• Logo
• Email address- Jess@orbellconsulting.com.au
• Contact number
• Services provided - Executive Coaching, Leadership, NLP and Motivational Mapping.
Nice to have
• Same colours as logo
Should not have
• Red or orange

```html
<!DOCTYPE html>
<html lang="en">
<head>
<meta charset="utf-8">
<title>Orbell Consulting – Business Card</title>
<link href="https://fonts.googleapis.com/css2?family=Montserrat:wght@600&family=Open+Sans:wght@400;600&display=swap" rel="stylesheet">
<style>
  :root {
    --backdrop: #5e5e5e;
    --card-light: #ffffff;
    --card-dark: #000000;
    --ink-dark: #111111;
    --ink-light: #ffffff;
  }
  html, body {
    margin: 0;
    width: 1200px;
    height: 900px;
    overflow: hidden;
    background: var(--backdrop);
    font-family: "Open Sans", Arial, sans-serif;
  }
  .canvas { position: relative; width: 1200px; height: 900px; }

  .card { position: absolute; top: 275px; width: 477px; height: 293px; }
  .card-front {
    left: 116px;
    background: var(--card-light);
    color: var(--ink-dark);
    border-radius: 0 48px 0 48px;
  }
  .card-back {
    left: 622px;
    top: 276px;
    height: 292px;
    background: var(--card-dark);
    color: var(--ink-light);
    border-radius: 48px 0 48px 0;
  }

  .brand-mark {
    position: absolute;
    left: 117px;
    top: 62px;
    width: 72px;
    height: 72px;
    border: 2px solid var(--ink-dark);
    border-radius: 50%;
    box-sizing: border-box;
  }
  .brand-name {
    position: absolute;
    font-family: "Montserrat", Arial, sans-serif;
    font-weight: 600;
    white-space: nowrap;
    letter-spacing: 0.2px;
  }
  .card-front .brand-name { left: 0; width: 310px; text-align: center; top: 139px; font-size: 23px; }
  .card-back .brand-name { left: 0; width: 480px; text-align: center; top: 86px; font-size: 29px; }

  .holder { position: absolute; right: 27px; top: 31px; text-align: right; }
  .holder-name { font-size: 17px; font-weight: 600; line-height: 22px; }
  .holder-role { font-size: 13px; line-height: 18px; }

  .contact-list {
    position: absolute;
    right: 26px;
    top: 207px;
    margin: 0;
    padding: 0;
    list-style: none;
    text-align: right;
    font-size: 13px;
    line-height: 20px;
  }
  .contact-list li { display: flex; justify-content: flex-end; align-items: center; gap: 5px; }
  .contact-list svg { width: 10px; height: 10px; fill: var(--ink-dark); }

  .services-heading {
    position: absolute;
    left: 0; right: 0;
    top: 194px;
    display: flex;
    align-items: center;
    gap: 9px;
    font-size: 18px;
    font-weight: 600;
  }
  .services-heading::before,
  .services-heading::after { content: ""; flex: 1; height: 2px; background: var(--ink-light); }
  .services-list {
    position: absolute;
    left: 0; right: 0;
    top: 223px;
    text-align: center;
    font-size: 13px;
    font-weight: 600;
    line-height: 17px;
  }
  .divider { margin: 0 5px; }
</style>
</head>
<body>
<main class="canvas">
  <section class="card card-front">
    <span class="brand-mark"></span>
    <div class="brand-name">ORBELL CONSULTING</div>
    <div class="holder">
      <div class="holder-name">Daniel Hartley</div>
      <div class="holder-role">Managing Director</div>
    </div>
    <ul class="contact-list">
      <li>(044)-312-5580
        <svg viewBox="0 0 10 10"><path d="M2 0.5 L3.6 2.6 L2.7 3.6 Q3.8 5.9 6.3 7.2 L7.3 6.3 L9.5 7.9 L8.4 9.5 Q1.5 8.2 0.5 1.6 Z"/></svg>
      </li>
      <li>info@orbellconsulting.com.au
        <svg viewBox="0 0 10 10"><path d="M0 2 H10 V8.5 H0 Z M0.8 2.6 L5 5.6 L9.2 2.6" stroke="#fff" stroke-width="0.9"/></svg>
      </li>
      <li>www.orbellconsulting.com.au
        <svg viewBox="0 0 10 10"><circle cx="5" cy="5" r="5"/><path d="M1 5 H9 M5 0.5 Q2.5 5 5 9.5 M5 0.5 Q7.5 5 5 9.5" stroke="#fff" stroke-width="0.8" fill="none"/></svg>
      </li>
    </ul>
  </section>

  <section class="card card-back">
    <div class="brand-name">ORBELL CONSULTING</div>
    <div class="services-heading">Services provided</div>
    <div class="services-list">
      Executive Coaching<span class="divider">|</span>Leadership<span class="divider">|</span>NLP<br>
      Motivational Mapping
    </div>
  </section>
</main>
</body>
</html>
```